Brightfold Partners Website

Brightfold Partners Advisory Services is a company which provides specialised advise in carbon markets, climate policy, landscapes, resilience and change. We are based in Australia but the majority of our business is global. Our clients range from governments to large corporates and not for profit organisations.
Our focus is on developing the capabilities of government officials, business decision makers and land managers so they can better navigate the complexity of climate change and sustainability.
We are looking for a website that is consistent with the high end professional services which we provide to serious players.
I have attached two versions of our logo. I have also attached the back of our business card so you can get a sense of what we hand to potential clients.

Target Market(s)

Professional individuals, decision makers, board members etc, government officials.

Industry/Entity Type

Government

Number of Pages Required

4 page

Font styles to use
Serif
Sans Serif

Requirements
Must have
• Please provide
• 1. Home page
• 2. Service page template
• 3. Contact page
• 4. Lead expert profile page

```html
<!DOCTYPE html>
<html lang="en">
<head>
<meta charset="utf-8">
<title>Brightfold Partners</title>
<link rel="stylesheet" href="https://fonts.googleapis.com/css2?family=Cinzel:wght@400;500;600&family=Oxygen:wght@400;700&family=Open+Sans:wght@400&display=swap">
<style>
:root{
  --ink:#2f2f2f;
  --text:#3a3a3a;
  --muted:#8e8e8e;
  --rule:#d4d4d4;
  --band:#ebebeb;
  --panel:#efefef;
  --footer-box:#3d3d3d;
  --footer-line:#555;
  --white:#fff;
}
*{margin:0;padding:0;box-sizing:border-box}
html,body{width:974px;height:1200px;overflow:hidden;background:var(--white)}
body{font-family:"Oxygen",sans-serif;color:var(--text);position:relative}
.abs{position:absolute}
.top-rule{left:0;top:0;width:974px;height:4px;background:#8a8a8a}
.header{left:0;top:4px;width:974px;height:96px;background:linear-gradient(#fff,#ececec);border-bottom:1px solid #d9d9d9}
.brand{left:105px;top:16px;display:flex;align-items:center;gap:12px}
.brand-dot{width:56px;height:56px;border-radius:50%;background:#555;flex-shrink:0}
.brand-name{font-family:"Cinzel",serif;font-weight:400;font-size:25px;line-height:29px;letter-spacing:2px;color:var(--ink);white-space:nowrap}
.call{left:727px;top:18px;display:flex;gap:8px;align-items:flex-start}
.call-small{font-size:12px;color:var(--ink)}
.call-number{font-size:19px;color:var(--ink);line-height:20px}
.nav{left:446px;top:77px;display:flex;font-size:12px;font-weight:700;color:#9a9a9a;white-space:nowrap}
.nav a{text-decoration:none;color:inherit;padding:0 14px;border-left:1px solid #c9c9c9;line-height:15px}
.nav a:first-child{padding-left:0;border-left:0;color:var(--ink)}
.hero{left:0;top:101px;width:974px;height:361px;background:linear-gradient(90deg,#9fb4c6 0%,#d7e1ea 30%,#1e2f57 45%,#b6cde6 55%,#d6e1ea 80%,#3a3a46 100%)}
.hero-arrow{top:155px;width:30px;height:30px;border-radius:50%;background:rgba(0,0,0,.75)}
.hero-caption{left:0;bottom:0;width:974px;height:36px;background:rgba(30,30,30,.6);color:var(--white);font-family:"Open Sans",sans-serif;font-size:21px;text-align:center;line-height:34px}
.section-title{font-family:"Cinzel",serif;font-size:20px;letter-spacing:1px;color:var(--ink);font-weight:500;white-space:nowrap}
.section-title .soft{color:var(--muted);font-weight:400}
.about-title{left:0;width:974px;top:480px;text-align:center;display:flex;justify-content:center;align-items:center;gap:8px}
.about-text{left:120px;top:518px;width:734px;font-size:10.2px;line-height:17px;text-align:center;color:var(--text)}
.services{left:0;top:606px;width:974px;height:219px;background:var(--band);border-top:1px solid #ddd;border-bottom:1px solid #ddd}
.services-title{left:0;width:974px;top:624px;text-align:center}
.service{top:663px;width:150px;text-align:center;font-size:11px;line-height:14px;color:var(--ink)}
.service-ring{width:106px;height:106px;margin:0 auto 10px;border:2px solid #444;border-radius:50%;background:var(--white);display:flex;align-items:center;justify-content:center}
.col-title{top:852px;font-size:16px;display:flex;align-items:center;gap:8px}
.col-rule{top:879px;height:1px;background:var(--rule)}
.news-item{left:115px;width:230px;font-size:10.4px;line-height:14.5px}
.news-date{font-weight:700;color:var(--ink);font-size:11px}
.more{font-size:10.5px;font-weight:700;color:var(--ink)}
.quote{left:372px;top:896px;width:228px;height:104px;background:var(--panel);border-radius:6px;padding:13px 6px 0 36px;font-size:10.2px;line-height:16px}
.quote-mark{left:386px;top:904px;font-family:"Cinzel",serif;font-size:34px;color:#c9c9c9;line-height:30px}
.avatar{left:388px;top:984px;width:54px;height:54px;border:2px solid #ddd;border-radius:4px;background:linear-gradient(#5c6d7c,#2d3b4a)}
.field{left:631px;width:229px;height:23px;border:1px solid #cfcfcf;border-radius:3px;font-size:10.5px;color:#777;padding:4px 8px;background:var(--white)}
.submit{left:630px;top:1024px;width:55px;height:19px;background:#3a3a3a;color:var(--white);font-size:11px;font-weight:700;text-align:center;line-height:19px;border-radius:2px}
.footer{left:0;top:1075px;width:974px;height:125px;background:linear-gradient(#333,#262626);border-top:2px solid #555}
.f-box{top:1091px;height:62px;background:var(--footer-box);border:1px solid var(--footer-line);padding:4px 9px;color:var(--white)}
.f-head{font-size:12.5px;font-weight:700}
.f-input{width:147px;height:22px;background:#5a5a5a;font-size:10.5px;color:#e0e0e0;padding:4px 7px;margin-top:7px;display:inline-block}
.f-go{width:25px;height:22px;background:#5a5a5a;display:inline-block;margin-left:4px;vertical-align:top;margin-top:7px}
.f-line{font-size:10px;color:#ddd;line-height:17px;display:flex;align-items:center;gap:8px;white-space:nowrap}
.f-line svg{flex-shrink:0}
.social-row{display:flex;gap:10px;margin-top:8px}
.social{width:20px;height:20px;border-radius:3px}
.f-brand{left:652px;top:1094px;display:flex;align-items:center;gap:12px}
.f-brand .brand-dot{background:#bbb;width:50px;height:50px}
.f-brand .brand-name{color:#e6e6e6;font-size:22px;line-height:27px}
.f-links{left:106px;top:1174px;font-size:10.2px;color:#e6e6e6;white-space:nowrap}
.copy{left:618px;top:1174px;font-size:10px;color:#e6e6e6;white-space:nowrap}
</style>
</head>
<body>
<div class="abs top-rule"></div>

<header class="abs header"></header>
<div class="abs brand"><div class="brand-dot"></div><div class="brand-name">BRIGHTFOLD<br>PARTNERS</div></div>
<div class="abs call">
  <svg width="26" height="26" viewBox="0 0 26 26"><circle cx="13" cy="13" r="12" fill="none" stroke="#888" stroke-width="1.5"/><path d="M9 7l3 0 1 4-2 1c1 2 2 3 4 4l1-2 4 1 0 3c-6 1-12-5-11-11z" fill="#666"/></svg>
  <div><div class="call-small">Call Us Today</div><div class="call-number">123 555 0190</div></div>
</div>
<nav class="abs nav"><a>HOME</a><a>OUR SERVICES</a><a>CONTACT US</a><a>LEAD EXPERT PROFILE</a></nav>

<div class="abs hero" role="img" aria-label="Photo of three business people discussing a bar chart on a wall screen">
  <div class="abs hero-arrow" style="left:35px"><svg width="30" height="30"><path d="M17 9l-6 6 6 6" fill="none" stroke="#fff" stroke-width="1.5"/></svg></div>
  <div class="abs hero-arrow" style="left:890px"><svg width="30" height="30"><path d="M13 9l6 6-6 6" fill="none" stroke="#fff" stroke-width="1.5"/></svg></div>
  <div class="abs hero-caption">Lorem ipsum dolor sit amet, consectetuer adipiscing elit sed diam</div>
</div>

<div class="abs about-title section-title"><svg width="24" height="24"><circle cx="12" cy="12" r="11" fill="#999"/></svg><span><span class="soft">ABOUT</span> BRIGHTFOLD PARTNERS</span></div>
<p class="abs about-text">Lorem ipsum dolor sit amet, consectetuer adipiscing elit,Sed diam nonummy nibh euismod tincidunt ut laoreet dolore magna aliquam erat volutpat. Ut wisi enim ad minim veniam, quis nostrud exerci tation ullamcorper suscipit lobortis nisl ut aliquip commodo consequat. Duis autem vel eum iriure dolor in hendrerit in vulputate velit esse molestie consequat, vel ill dolore eu feugiat nulla facilisis at vero eros et accumsan et iusto odio dignissim qui blandit praesent luptatumdeelenit augue duis dolore te feugait nulla facilisi.</p>

<section class="abs services"></section>
<div class="abs services-title section-title"><span class="soft">OUR</span> SERVICES</div>
<div class="abs service" style="left:107px"><div class="service-ring"><svg width="64" height="60" viewBox="0 0 64 60"><circle cx="22" cy="26" r="11" fill="#222"/><path d="M2 56c0-12 8-18 20-18s20 6 20 18z" fill="#222"/><path d="M44 2a14 12 0 1 1-9 21l-6 5 2-8a14 12 0 0 1 13-18z" fill="#fff" stroke="#222" stroke-width="2.5"/><circle cx="45" cy="8" r="2" fill="#222"/><path d="M45 12v10" stroke="#222" stroke-width="3"/></svg></div>Corporate Advisory on<br>Carbon Markets</div>
<div class="abs service" style="left:252px"><div class="service-ring"><svg width="60" height="60"><circle cx="22" cy="36" r="14" fill="none" stroke="#222" stroke-width="7" stroke-dasharray="5 3"/><circle cx="42" cy="18" r="10" fill="none" stroke="#222" stroke-width="6" stroke-dasharray="4 3"/></svg></div>Project Mechanisms<br>(carbon credits &amp; offsets)</div>
<div class="abs service" style="left:412px"><div class="service-ring"><svg width="64" height="60"><path d="M4 4v50h56" fill="none" stroke="#222" stroke-width="3"/><rect x="12" y="38" width="8" height="14" fill="#222"/><rect x="24" y="32" width="8" height="20" fill="#222"/><rect x="36" y="36" width="8" height="16" fill="#222"/><rect x="48" y="24" width="8" height="28" fill="#222"/><path d="M10 30l12-12 10 8 18-16" fill="none" stroke="#222" stroke-width="3"/><path d="M44 8h8v8" fill="none" stroke="#222" stroke-width="3"/></svg></div>Monitoring, Reporting<br>&amp; Verification</div>
<div class="abs service" style="left:563px"><div class="service-ring"><svg width="64" height="60"><path d="M32 4l28 12H4z" fill="#222"/><rect x="6" y="18" width="52" height="4" fill="#222"/><rect x="10" y="25" width="6" height="22" fill="#222"/><rect x="21" y="25" width="6" height="22" fill="#222"/><rect x="32" y="25" width="6" height="22" fill="#222"/><rect x="43" y="25" width="6" height="22" fill="#222"/><rect x="4" y="50" width="56" height="5" fill="#222"/></svg></div>Institutional<br>Arrangements</div>
<div class="abs service" style="left:701px"><div class="service-ring"><svg width="60" height="60"><rect x="10" y="14" width="40" height="28" fill="none" stroke="#222" stroke-width="3"/><path d="M18 34l8-8 6 5 10-10" fill="none" stroke="#222" stroke-width="3"/><path d="M30 42v12M22 54h16" stroke="#222" stroke-width="3"/></svg></div>Training &amp;<br>Coaching</div>

<div class="abs col-title section-title" style="left:115px"><svg width="20" height="16"><path d="M1 5h5l10-4v14L6 11H1z" fill="#555"/></svg><span><span class="soft">LATEST</span> NEWS</span></div>
<div class="abs col-rule" style="left:115px;width:230px"></div>
<div class="abs news-item" style="top:893px"><div class="news-date">11/12/2013</div>Lorem ipsum dolor sit amet, cctetuer adipiscingin elit, sed diam nummy nibh eui smod tinciduntiot vulputate velit esse molestie</div>
<div class="abs" style="left:115px;top:957px;width:226px;border-top:1px dashed #ccc"></div>
<div class="abs news-item" style="top:964px"><div class="news-date">11/4/2012</div>Lorem ipsum dolor sit amet, cctetuer adipiscingin elit, sed diam nummy nibh eui smod tinciduntiot vulputate velit esse molestie</div>
<div class="abs more" style="left:285px;top:1033px">Read more »</div>

<div class="abs col-title section-title" style="left:372px"><svg width="20" height="18"><rect x="1" y="1" width="14" height="10" rx="2" fill="#555"/><rect x="6" y="6" width="13" height="9" rx="2" fill="#777"/></svg><span><span class="soft">CLIENT</span> TESTIMONIAL</span></div>
<div class="abs col-rule" style="left:372px;width:228px"></div>
<div class="abs quote">Duis autem vel eum iriureol hder in vultat velit esse moles conqat vela ilu dolor feugiat.Duis autem vel eum ure hendrern vultat velit esse autm vel eum iriure dol</div>
<div class="abs quote-mark">“</div>
<div class="abs avatar" role="img" aria-label="Client portrait photo"></div>
<div class="abs" style="left:455px;top:1013px;font-size:10.5px;color:var(--ink)">Mr. Dolore Eu Feugiat</div>
<div class="abs more" style="left:545px;top:1035px">Read more »</div>

<div class="abs col-title section-title" style="left:631px"><svg width="16" height="16"><path d="M2 2h9M2 2v12h12V7" fill="none" stroke="#555" stroke-width="2"/><path d="M7 10l7-7" stroke="#555" stroke-width="2"/></svg><span><span class="soft">QUICK</span> CONTACT</span></div>
<div class="abs col-rule" style="left:631px;width:229px"></div>
<div class="abs field" style="top:895px">Name</div>
<div class="abs field" style="top:924px">Email</div>
<div class="abs field" style="top:953px;height:58px">Message</div>
<div class="abs submit">Submit</div>

<footer class="abs footer"></footer>
<div class="abs f-box" style="left:105px;width:199px"><div class="f-head">Subscribe to Newsletter</div><span class="f-input">Email here</span><span class="f-go"><svg width="25" height="22"><path d="M10 6l5 5-5 5" fill="none" stroke="#fff" stroke-width="2"/></svg></span></div>
<div class="abs f-box" style="left:345px;width:123px"><div class="f-head">Contact Us</div><div class="f-line"><svg width="10" height="10"><path d="M1 1h3l1 3-2 1 3 3 1-2 3 1v3C5 10 0 5 1 1z" fill="#999"/></svg>012-555-0148</div><div class="f-line"><svg width="10" height="8"><rect x="0.5" y="0.5" width="9" height="7" fill="none" stroke="#999"/><path d="M1 1l4 3 4-3" fill="none" stroke="#999"/></svg>info@brightfold.com</div></div>
<div class="abs f-box" style="left:510px;width:96px"><div class="f-head">Follow Us</div><div class="social-row"><span class="social" style="background:#3b5a98"></span><span class="social" style="background:#3ea6d9"></span><span class="social" style="background:#f07b1f"></span></div></div>
<div class="abs f-brand"><div class="brand-dot"></div><div class="brand-name">BRIGHTFOLD<br>PARTNERS</div></div>
<div class="abs f-links">Home &nbsp;|&nbsp; Our Services | &nbsp;Contact Us &nbsp;| &nbsp;Lead Export Profile</div>
<div class="abs copy">Copyright © 2014 Brightfold Partners. All Rights Reserved</div>
</body>
</html>
```